Food and Beverage Business Cards

We need business cards with logo designs for a consultant in the food and beverage industry. We specialize in helping restaurants fix operational and management problems.
Specific areas of expertise include:
-Steps of service
-Staff management tools
-Standard operating procedures
-Profit and loss management
-Inventory
-Point of sales
-Bar Menu
-Mystery shopper service
-Handling and managing suppliers

Target Market(s)

Restaurant and bar owners and managers

Industry/Entity Type

Business

Contact Information for Business Card

Mathieu Delorme
K&T Consulting
phone: 15027390618
mathkt@brindlemail.net

Font styles to use
Other font styles liked:
• Check out the screen shot font idea

Colors

Designer to choose colors to be used in the design.

Requirements
Must have
• Must include QR code (See attachment)
• Logo should reflect our specific focus on the drinks side of the industry.
• Areas of Expertise:
• -Service Steps
• -Staff management tools
• -S.O.P
• -P&L Management
• -Inventory
• -P.O.S
• -Bar Menu
• -Mystery Shopper Service
• -Handling and Managing Suppliers

```html
<!DOCTYPE html>
<html lang="en">
<head>
<meta charset="utf-8">
<title>K&amp;T Consulting – Business Card</title>
<link rel="stylesheet" href="https://fonts.googleapis.com/css2?family=Open+Sans:wght@400;600;700&display=swap">
<style>
  :root {
    --page-bg: #e9e6e2;
    --card-white: #ffffff;
    --brand-red: #c21416;
    --ink-black: #0d0d0d;
    --back-black: #121212;
    --pattern-grey: #1f1f1f;
    --text-light: #ffffff;
    --font-main: "Open Sans", Arial, sans-serif;
  }
  html, body {
    margin: 0;
    padding: 0;
    width: 1200px;
    height: 900px;
    overflow: hidden;
    background: var(--page-bg);
    font-family: var(--font-main);
  }
  .canvas {
    position: relative;
    width: 1200px;
    height: 900px;
  }
  .card {
    position: absolute;
    overflow: hidden;
    box-shadow: 0 6px 18px rgba(0,0,0,0.18);
  }

  /* Front */
  .card-front {
    left: 178px;
    top: 74px;
    width: 588px;
    height: 363px;
    background: var(--card-white);
  }
  .front-bands {
    position: absolute;
    inset: 0;
  }
  .brand-name {
    position: absolute;
    left: 0;
    right: 0;
    top: 78px;
    margin: 0;
    text-align: center;
    font-size: 50px;
    line-height: 68px;
    font-weight: 600;
    color: var(--brand-red);
  }
  .person {
    position: absolute;
    right: 325px;
    top: 257px;
    text-align: right;
    color: var(--text-light);
  }
  .person-name {
    margin: 0;
    font-size: 18px;
    font-weight: 600;
    line-height: 24px;
    text-transform: uppercase;
  }
  .person-title {
    margin: 0;
    font-size: 15px;
    font-weight: 400;
    line-height: 20px;
  }
  .contact-list {
    position: absolute;
    left: 287px;
    top: 246px;
    margin: 0;
    padding: 0;
    list-style: none;
    color: var(--text-light);
    font-size: 14.5px;
    line-height: 21px;
  }
  .contact-list li {
    display: flex;
    align-items: center;
    gap: 6px;
  }
  .contact-icon {
    width: 11px;
    height: 11px;
    flex: none;
  }
  .address {
    position: absolute;
    left: 0;
    right: 0;
    top: 318px;
    margin: 0;
    text-align: center;
    color: var(--text-light);
    font-size: 14.5px;
    line-height: 20px;
  }

  /* Back */
  .card-back {
    left: 388px;
    top: 505px;
    width: 567px;
    height: 352px;
    background: var(--back-black);
  }
  .back-pattern {
    position: absolute;
    inset: 0;
    background: linear-gradient(160deg, var(--pattern-grey) 0%, var(--back-black) 55%, var(--pattern-grey) 100%);
  }
  .back-brand {
    position: absolute;
    left: 382px;
    top: 177px;
    transform: translate(-50%, -50%);
    margin: 0;
    font-size: 17px;
    line-height: 22px;
    font-weight: 600;
    color: var(--brand-red);
    white-space: nowrap;
  }
</style>
</head>
<body>
<main class="canvas">

  <section class="card card-front" aria-label="Business card front">
    <svg class="front-bands" width="588" height="363" viewBox="0 0 588 363" aria-hidden="true">
      <path d="M0,192 Q294,272 588,184" fill="none" stroke="var(--ink-black)" stroke-width="7"/>
      <path d="M0,198 Q294,274 588,190 L588,363 L0,363 Z" fill="var(--brand-red)"/>
    </svg>

    <h1 class="brand-name">K&amp;T Consulting</h1>

    <div class="person">
      <p class="person-name">Mathieu Delorme</p>
      <p class="person-title">Managing Director</p>
    </div>

    <ul class="contact-list">
      <li>
        <svg class="contact-icon" viewBox="0 0 12 12" aria-hidden="true">
          <path d="M2.5 0.8 L4.3 3.6 L3.2 4.7 Q4.3 7.4 7.3 8.8 L8.4 7.7 L11.2 9.5 L10 11.4 Q4.6 11.2 0.6 2 Z" fill="var(--text-light)"/>
        </svg>
        <span>15027390618</span>
      </li>
      <li>
        <svg class="contact-icon" viewBox="0 0 12 12" aria-hidden="true">
          <rect x="0.5" y="2.5" width="11" height="7.5" fill="var(--text-light)"/>
          <path d="M0.8 2.8 L6 6.8 L11.2 2.8" fill="none" stroke="var(--brand-red)" stroke-width="1"/>
        </svg>
        <span>mathkt@brindlemail.net</span>
      </li>
      <li>
        <svg class="contact-icon" viewBox="0 0 12 12" aria-hidden="true">
          <circle cx="6" cy="6" r="5.2" fill="none" stroke="var(--text-light)" stroke-width="1.2"/>
          <ellipse cx="6" cy="6" rx="2.2" ry="5.2" fill="none" stroke="var(--text-light)" stroke-width="1"/>
          <line x1="0.8" y1="6" x2="11.2" y2="6" stroke="var(--text-light)" stroke-width="1"/>
        </svg>
        <span>www.ktconsulting-bar.com</span>
      </li>
    </ul>

    <p class="address">12345, Address Goes Here, Country Name here, 123456.</p>
  </section>

  <section class="card card-back" aria-label="Business card back">
    <div class="back-pattern" role="img" aria-label="Faint repeating brand pattern in dark grey across the card back"></div>
    <p class="back-brand">K&amp;T Consulting</p>
  </section>

</main>
</body>
</html>
```